Data Visualization (graphs, tables, models, circles)

We need an intuitive - user friendly - and fresh design line for our data visualization.

You know. Keep The Path Clear!

Our core product is based on the presentation and interpretation of different data sources that we combine into graphs, tables, charts etc and make visible to clients through a web platform and or Reports. Our business area is Search & Social Media Intelligence.

See Trevla.com for some inspiration in terms of current colors and a better understanding of the company. Our Logo / Name is the only one thing that cannot be changed. Everything else is up to you. Feel free to ask questions.

I have attached a few screenshots of some of our features and as you can see - there has never been a designer on this assignment. We are looking for a long term relationship with a designer that can work with us on an ongoing basis.

Design of graphs/models/circles/tables needs to be able to fit into Infographics also.

We are basically looking for an identity for our data visualization. Meaning that readers / target audience can recognize our graphs and say: Check out the cool graphs by Trevla :-)

Think: Zorbix, PlumLedger, etc. in terms of data presentation.
Updates

Project Deadline Extended
Reason: Due to illness we lost a few days last week and have not have sufficient time to look through the different designs.

Target Market(s)

Marketing People, CEO's, Strategic Planners, Ad Agencies, Decision Makers

Industry/Entity Type

Business

Requirements
Must have
• Must present at least 1 line graph (like file 1 and 2), 1 pie chart, 1 column graph and 1 matrix (like file3).

```html
<!DOCTYPE html>
<html lang="en">
<head>
<meta charset="utf-8">
<title>Keyword Discovery - Top Related Keywords</title>
<link rel="stylesheet" href="https://fonts.googleapis.com/css2?family=Nunito+Sans:wght@300;400;600;700&display=swap">
<style>
  :root {
    --brand-red: #d0021b;
    --rule-red: #e25466;
    --text-grey: #555555;
    --box-grey: #9a9a9a;
    --link-grey: #a8a8a8;
    --paper: #ffffff;
  }
  * { margin: 0; padding: 0; box-sizing: border-box; }
  html, body { width: 1200px; height: 984px; overflow: hidden; background: var(--paper); }
  body { font-family: "Nunito Sans", Arial, sans-serif; }
  .canvas { position: relative; width: 1200px; height: 984px; }

  .page-title {
    position: absolute; left: 104px; top: 87px;
    font-size: 27px; font-weight: 300; color: var(--brand-red); letter-spacing: 0.3px;
    line-height: 34px;
  }
  .rule { position: absolute; left: 98px; width: 969px; height: 1px; background: var(--rule-red); }
  .rule--top { top: 131px; }
  .rule--bottom { top: 880px; }
  .credit {
    position: absolute; left: 98px; top: 895px;
    font-size: 14px; color: var(--brand-red); letter-spacing: 0.1px;
  }

  .links { position: absolute; left: 0; top: 0; }
  .links line { stroke: var(--link-grey); stroke-width: 1; }

  .seed {
    position: absolute; left: 173px;
    font-size: 22px; font-weight: 600; color: var(--brand-red);
    line-height: 28px;
  }
  .node {
    position: absolute; width: 138px; height: 41px;
    border-radius: 4px; border: 2px dotted;
    display: flex; align-items: center; justify-content: center;
    font-size: 19.5px; font-weight: 300; color: var(--text-grey);
    background: var(--paper);
  }
  .node--primary { border-color: var(--brand-red); }
  .node--secondary { border-color: var(--box-grey); }
</style>
</head>
<body>
<div class="canvas">
  <h1 class="page-title">Keyword Discovery - Top Related Keywords</h1>
  <div class="rule rule--top"></div>

  <svg class="links" width="1200" height="984" viewBox="0 0 1200 984" aria-hidden="true">
    <line x1="291" y1="378" x2="402" y2="303"/>
    <line x1="291" y1="378" x2="402" y2="377"/>
    <line x1="291" y1="378" x2="402" y2="447"/>
    <line x1="540" y1="305" x2="705" y2="226"/>
    <line x1="540" y1="305" x2="705" y2="282"/>
    <line x1="540" y1="305" x2="705" y2="339"/>
    <line x1="540" y1="305" x2="705" y2="404"/>
    <line x1="540" y1="305" x2="705" y2="468"/>
    <line x1="540" y1="305" x2="705" y2="529"/>
    <line x1="291" y1="704" x2="401" y2="626"/>
    <line x1="291" y1="704" x2="401" y2="704"/>
    <line x1="291" y1="704" x2="401" y2="773"/>
  </svg>

  <div class="seed" style="top:364px">Keyword 1</div>
  <div class="node node--primary" style="left:402px;top:286px">Keyword A</div>
  <div class="node node--primary" style="left:402px;top:356px">Keyword B</div>
  <div class="node node--primary" style="left:402px;top:425px">Keyword C</div>

  <div class="node node--secondary" style="left:705px;top:203px">Keyword G</div>
  <div class="node node--secondary" style="left:705px;top:262px">Keyword H</div>
  <div class="node node--secondary" style="left:705px;top:319px">Keyword I</div>
  <div class="node node--secondary" style="left:705px;top:384px">Keyword J</div>
  <div class="node node--secondary" style="left:705px;top:446px">Keyword K</div>
  <div class="node node--secondary" style="left:705px;top:505px">Keyword L</div>

  <div class="seed" style="top:690px">Keyword 2</div>
  <div class="node node--primary" style="left:401px;top:614px">Keyword D</div>
  <div class="node node--primary" style="left:401px;top:684px">Keyword E</div>
  <div class="node node--primary" style="left:401px;top:754px">Keyword F</div>

  <div class="rule rule--bottom"></div>
  <p class="credit">All images and data are property of Trevla Technology SA</p>
</div>
</body>
</html>
```